Business card design

I have a PDF of just what I want, but I need it to be digitized for Harlow Depot so I can edit and modify for new employees and reorder going forward

Business

```html
<!DOCTYPE html>
<html lang="en">
<head>
<meta charset="utf-8">
<title>TIDE Property Managers – Business Card</title>
<link rel="stylesheet" href="https://fonts.googleapis.com/css2?family=Arimo:wght@400;700&display=swap">
<style>
  :root {
    --page-bg: #e9e6e1;
    --card-cyan-light: #3cc6ea;
    --card-cyan: #22aedb;
    --card-cyan-deep: #168fbd;
    --band-dark: #31363b;
    --band-dark-edge: #24282c;
    --rule-light: #dff4fb;
    --text-white: #ffffff;
    --skyline-grey: #4a5258;
    --card-shadow: rgba(0, 0, 0, 0.28);
  }
  * { box-sizing: border-box; margin: 0; padding: 0; }
  html, body {
    width: 1200px;
    height: 1024px;
    overflow: hidden;
    background: var(--page-bg);
  }
  .canvas {
    position: relative;
    width: 1200px;
    height: 1024px;
  }
  .business-card {
    position: absolute;
    left: 340px;
    top: 57px;
    width: 520px;
    height: 910px;
    border-radius: 6px;
    overflow: hidden;
    background: linear-gradient(160deg, var(--card-cyan-light) 0%, var(--card-cyan) 45%, var(--card-cyan-deep) 100%);
    box-shadow: 0 18px 40px var(--card-shadow);
    font-family: "Arimo", Arial, sans-serif;
    color: var(--text-white);
  }
  .brand-band {
    position: absolute;
    left: 0;
    top: 70px;
    width: 100%;
    height: 200px;
    background: linear-gradient(180deg, var(--band-dark) 0%, var(--band-dark-edge) 100%);
    border-top: 5px solid var(--rule-light);
    border-bottom: 5px solid var(--rule-light);
    text-align: center;
  }
  .brand-name {
    display: block;
    padding-top: 22px;
    font-size: 104px;
    font-weight: 700;
    line-height: 1;
    letter-spacing: 2px;
  }
  .brand-tagline {
    display: block;
    margin-top: 4px;
    font-size: 40px;
    font-weight: 700;
    line-height: 1.1;
  }
  .contact-person {
    position: absolute;
    left: 0;
    top: 330px;
    width: 100%;
    text-align: center;
  }
  .person-name,
  .person-role,
  .person-mobile {
    font-size: 42px;
    font-weight: 400;
    line-height: 1.22;
  }
  .office-details {
    position: absolute;
    left: 0;
    top: 500px;
    width: 100%;
    text-align: center;
    font-style: normal;
    font-size: 24px;
    line-height: 1.38;
  }
  .skyline-artwork {
    position: absolute;
    left: 40px;
    bottom: 40px;
    width: 440px;
    height: 150px;
    border-radius: 4px;
    background: linear-gradient(180deg, rgba(74, 82, 88, 0.35) 0%, var(--skyline-grey) 100%);
  }
</style>
</head>
<body>
<main class="canvas">
  <article class="business-card">
    <header class="brand-band">
      <span class="brand-name">TIDE</span>
      <span class="brand-tagline">Property Managers</span>
    </header>

    <section class="contact-person">
      <p class="person-name">Maren Ashby</p>
      <p class="person-role">Director/ Manager</p>
      <p class="person-mobile">022 555 0147</p>
    </section>

    <address class="office-details">
      G4, 28 Wharf Lane,<br>
      Harbour Quarter, Kelston City<br>
      Ph: (09) 555 0193<br>
      Fax: (09) 555 0194<br>
      Email: info@tidelivingsuites.co.nz<br>
      www.tidelivingsuites.co.nz
    </address>

    <div class="skyline-artwork" role="img" aria-label="City harbour skyline silhouette with a tall tower and a sailboat"></div>
  </article>
</main>
</body>
</html>
```